oneness poster

a clean, elegant, simple text poster as follows (with some sort of glow or background consistent with the message:
MANIFESTO OF QUIET RIVERS

1. I am part of the world. The world is not outside of me, and I am not outside of the world. The world is in me, and I am in the world.

2. I am part of nature, and nature is part of me. I am what I am in my communication and communion with all living things. I am an irreducible and coherent whole with the web of life on the planet.

3. I am part of society, and society is part of me. I am what I am in my communication and communion with my fellow humans. I am an irreducible and coherent whole with the community of humans on the planet.

4. I am more than a skin-and-bone material organism: my body, and its cells and organs are manifestations of what is truly me: a self-sustaining, self-evolving dynamic system arising, persisting and evolving in interaction with everything around me.

5. I am one of the highest, most evolved manifestations of the drive toward coherence and wholeness in the universe. All systems drive toward coherence and wholeness in interaction with all other systems, and my essence is this cosmic drive. It is the same essence, the same spirit that is inherent in all the things that arise and evolve in nature, whether on this planet or elsewhere in the infinite reaches of space and time.

6. There are no absolute boundaries and divisions in this world, only transition points where one set of relations yields prevalence to another. In me, in this self-maintaining and self-evolving coherence- and wholeness-oriented system, the relations that integrate the cells and organs of my body are prevalent. Beyond my body other relations gain prevalence: those that drive toward coherence and wholeness in society and in nature.

7. The separate identity I attach to other humans and other things is but a convenient convention that facilitates my interaction with them. My family and my community are just as much “me” as the organs of my body. My body and mind, my family and my community, are interacting and interpenetrating, variously prevalent elements in the network of relations that encompasses all things in nature and the human world.

8. The whole gamut of concepts and ideas that separates my identity, or the identity of any person or community, from the identity of other persons and communities are manifestations of this convenient but arbitrary convention. There are only gradients distinguishing individuals from each other and from their environment and no real divisions and boundaries. There are no “others” in the world: we are all living systems and we are all part of each other.

9. Attempting to maintain the system I know as “me” through ruthless competition with the system I know as “you” is a grave mistake: it could damage the integrity of the embracing whole that frames both your life and mine. I cannot preserve my own life and wholeness by damaging that whole, even if damaging a part of it seems to bring me short-term advantage. When I harm you, or anyone else around me, I harm myself.

10. Collaboration, not competition, is the royal road to the wholeness that hallmarks healthy systems in the world. Collaboration calls for empathy and solidarity, and ultimately for love. I do not and cannot love myself if I do not love you and others around me: we are part of the same whole and so are part of each other.

11. The idea of “self-defense” even of “national defense,” needs to be rethought. Patriotism if it aims to eliminate adversaries by force, and heroism even in the well-meaning execution of that aim, are mistaken aspirations. A patriot and a hero who brandishes a sword or a gun is an enemy also to himself. Every weapon intended to hurt or kill is a danger to all. Comprehension, conciliation and forgiveness are not signs of weakness; they are signs of courage.

12. “The good” for me and for every person in the world is not the possession and accumulation of personal wealth. Wealth, in money or in any material resource, is but a means for maintaining myself in my environment. As exclusively mine, it commandeers part of the resources that all things need to share if they are to live and to thrive. Exclusive wealth is a threat to all people in the human community. And because I am a part of this community, in the final count it is a threat also to me, and to all who hold it.

13. Beyond the sacred whole we recognize as the world in its totality, only life and its development have what philosophers call intrinsic value; all other things have merely instrumental value: value insofar as they add to or enhance intrinsic value. Material things in the world, and the energies and substances they harbor or generate, have value only if and insofar they contribute to life and wellbeing in the web of life on this Earth.

14. Every healthy person has pleasure in giving: it is a higher pleasure than having. I am healthy and whole when I value giving over having. The true measure of my accomplishment and excellence is my readiness to give. Not the amount of what I give is the measure of my accomplishment and excellence, but the relation between what I give, and what my family and I need to live and to thrive.

15. A community that values giving over having is a community of healthy people, oriented toward thriving through empathy, solidarity, and love among its members. Sharing enhances the community of life, while possessing and accumulating creates demarcation, invites competition, and fuels envy. The share-society is the norm for all the communities of life on the planet; the have-society is typical only of modern-day humanity, and it is an aberration.
.

16. I acknowledge my role and responsibility in evolving a planetary consciousness in me, and by example in others around me. I have been part of the aberration of human consciousness in the modern age, and now wish to become part of the evolution that overcomes the aberration and heals the wounds inflicted by it. This is my right as well as my duty, as a conscious member of a conscious species on a precious and now critically endangered planet.

• MANIFESTO OF QUIET RIVERS

.

• a very very simple glow in the background or other look consistent with the all-is-one (OM) message. A strong, almost spirtual feel.
• no flowery designs, no distractions. Nothing cute.

```html
<!DOCTYPE html>
<html lang="en">
<head>
<meta charset="utf-8">
<title>Manifesto of Quiet Rivers</title>
<link href="https://fonts.googleapis.com/css2?family=Oswald:wght@500;700&family=Roboto+Condensed:wght@400&display=swap" rel="stylesheet">
<style>
  :root {
    --ink: #000000;
    --red: #e2231a;
    --text: #f2f2f2;
    --earth-deep: #0b1f3f;
    --earth-mid: #2f5f97;
    --earth-light: #c9d6e6;
  }
  * { margin: 0; padding: 0; box-sizing: border-box; }
  html, body { width: 800px; height: 1200px; overflow: hidden; background: var(--ink); }
  .poster {
    position: relative; width: 800px; height: 1200px; overflow: hidden;
    background: var(--ink); color: var(--text);
    font-family: "Roboto Condensed", "Arial Narrow", sans-serif;
  }
  .poster-title {
    position: absolute; top: 22px; left: 0; width: 800px; text-align: center;
    font-family: "Oswald", sans-serif; font-weight: 700; font-size: 62px;
    letter-spacing: 2px; color: var(--red); line-height: 1;
  }
  .earth {
    position: absolute; left: 190px; top: 400px; width: 420px; height: 420px; border-radius: 50%;
    background: radial-gradient(circle at 42% 38%, var(--earth-light) 0%, var(--earth-mid) 35%, var(--earth-deep) 75%, #020611 100%);
    box-shadow: 0 0 60px rgba(120,160,220,0.25);
  }
  .earth-caption {
    position: absolute; left: 300px; top: 560px; width: 200px; text-align: center;
    font-family: "Oswald", sans-serif; font-weight: 500; font-size: 24px; line-height: 1.05;
    color: var(--red);
  }
  .tenet { position: absolute; }
  .tenet h2 {
    font-family: "Oswald", sans-serif; font-weight: 500; font-size: 14px; line-height: 1.1;
    color: var(--red); text-transform: uppercase; margin-bottom: 4px;
  }
  .tenet p { font-size: 8.4px; line-height: 1.28; color: var(--text); }
  .side-column { position: absolute; top: 418px; width: 178px; display: flex; flex-direction: column; gap: 12px; }
  .side-column .tenet { position: static; }
  .side-left { left: 22px; }
  .side-right { left: 600px; }
</style>
</head>
<body>
<main class="poster">
  <h1 class="poster-title">MANIFESTO OF QUIET RIVERS</h1>

  <section class="tenet" style="left:22px; top:128px; width:350px;">
    <h2>1. I am part of the world</h2>
    <p>The world is not outside of me, and I am not outside of the world. The world is in me, and I am in the world.</p>
  </section>
  <section class="tenet" style="left:400px; top:128px; width:180px;">
    <h2>2. I am part of nature</h2>
    <p>and nature is part of me. I am what I am in my communication and communion with all living things. I am an irreducible and coherent whole with the web of life on the planet.</p>
  </section>
  <section class="tenet" style="left:600px; top:128px; width:178px;">
    <h2>3. I am part of society</h2>
    <p>and society is part of me. I am what I am in my communication and communion with my fellow humans. I am an irreducible and coherent whole with the community of humans on the planet.</p>
  </section>

  <section class="tenet" style="left:22px; top:218px; width:350px;">
    <h2>4. The whole gamut</h2>
    <p>of concepts and ideas that separates my identity, or the identity of any person or community, from the identity of other persons and communities are manifestations of this convenient but arbitrary convention. There are only gradients distinguishing individuals from each other and from their environment and no real divisions and boundaries. There are no “others” in the world: we are all living systems and we are all part of each other.</p>
  </section>
  <section class="tenet" style="left:400px; top:218px; width:180px;">
    <h2>5. I am one of the highest</h2>
    <p>most evolved manifestations of the drive toward coherence and wholeness in the universe. All systems drive toward coherence and wholeness in interaction with all other systems, and my essence is this cosmic drive. It is the same essence, the same spirit that is inherent in all the things that arise and evolve in nature, whether on this planet or elsewhere in the infinite reaches of space and time.</p>
  </section>
  <section class="tenet" style="left:600px; top:218px; width:178px;">
    <h2>6. There are no absolute</h2>
    <p>boundaries and divisions in this world, only transition points where one set of relations yields prevalence to another. In me, in this self-maintaining and self-evolving system, the relations that integrate the cells and organs of my body are prevalent. Beyond my body other relations gain prevalence: those that drive toward coherence and wholeness in society and in nature.</p>
  </section>

  <div class="earth" role="img" aria-label="Photograph of planet Earth seen from space"></div>
  <p class="earth-caption">I AM<br>PART OF<br>THE WORLD</p>

  <div class="side-column side-left">
    <section class="tenet">
      <h2>7. The separate identity</h2>
      <p>I attach to other humans and other things is but a convenient convention that facilitates my interaction with them. My family and my community are just as much “me” as the organs of my body. My body and mind, my family and my community, are interacting and interpenetrating, variously prevalent elements in the network of relations that encompasses all things in nature and the human world.</p>
    </section>
    <section class="tenet">
      <h2>9. Collaboration</h2>
      <p>not competition, is the royal road to the wholeness that hallmarks healthy systems in the world. Collaboration calls for empathy and solidarity, and ultimately for love. I do not and cannot love myself if I do not love you and others around me: we are part of the same whole and so are part of each other.</p>
    </section>
    <section class="tenet">
      <h2>11. The idea of</h2>
      <p>“self-defense” even of “national defense,” needs to be rethought. Patriotism if it aims to eliminate adversaries by force, and heroism even in the well-meaning execution of that aim, are mistaken aspirations. A patriot and a hero who brandishes a sword or a gun is an enemy also to himself. Every weapon intended to hurt or kill is a danger to all. Comprehension, conciliation and forgiveness are not signs of weakness; they are signs of courage.</p>
    </section>
  </div>

  <div class="side-column side-right">
    <section class="tenet">
      <h2>8. Attempting to maintain</h2>
      <p>the system I know as “me” through ruthless competition with the system I know as “you” is a grave mistake: it could damage the integrity of the embracing whole that frames both your life and mine. I cannot preserve my own life and wholeness by damaging that whole, even if damaging a part of it seems to bring me short-term advantage. When I harm you, or anyone else around me, I harm myself.</p>
    </section>
    <section class="tenet">
      <h2>10. I am more</h2>
      <p>than a skin-and-bone material organism: my body, and its cells and organs are manifestations of what is truly me: a self-sustaining, self-evolving dynamic system arising, persisting and evolving in interaction with everything around me.</p>
    </section>
    <section class="tenet">
      <h2>12. A community</h2>
      <p>that values giving over having is a community of healthy people, oriented toward thriving through empathy, solidarity, and love among its members. Sharing enhances the community of life, while possessing and accumulating creates demarcation, invites competition, and fuels envy. The share-society is the norm for all the communities of life on the planet; the have-society is typical only of modern-day humanity, and it is an aberration.</p>
    </section>
  </div>

  <section class="tenet" style="left:22px; top:940px; width:350px;">
    <h2>13. Every healthy person</h2>
    <p>has pleasure in giving: it is a higher pleasure than having. I am healthy and whole when I value giving over having. The true measure of my accomplishment and excellence is my readiness to give. Not the amount of what I give is the measure of my accomplishment and excellence, but the relation between what I give, and what my family and I need to live and to thrive.</p>
  </section>
  <section class="tenet" style="left:400px; top:940px; width:180px;">
    <h2>14. Beyond the sacred whole</h2>
    <p>we recognize as the world in its totality, only life and its development have what philosophers call intrinsic value; all other things have merely instrumental value: value insofar as they add to or enhance intrinsic value. Material things in the world, and the energies and substances they harbor or generate, have value only if and insofar they contribute to life and wellbeing in the web of life on this Earth.</p>
  </section>
  <section class="tenet" style="left:600px; top:940px; width:178px;">
    <h2>15. I acknowledge my role</h2>
    <p>and responsibility in evolving a planetary consciousness in me, and by example in others around me. I have been part of the aberration of human consciousness in the modern age, and now wish to become part of the evolution that overcomes the aberration and heals the wounds inflicted by it. This is my right as well as my duty, as a conscious member of a conscious species on a precious and now critically endangered planet.</p>
  </section>
  <section class="tenet" style="left:400px; top:1080px; width:378px;">
    <h2>16. “The good” for me</h2>
    <p>and for every person in the world is not the possession and accumulation of personal wealth. Wealth, in money or in any material resource, is but a means for maintaining myself in my environment. As exclusively mine, it commandeers part of the resources that all things need to share if they are to live and to thrive. Exclusive wealth is a threat to all people in the human community. And because I am a part of this community, in the final count it is a threat also to me, and to all who hold it.</p>
  </section>
</main>
</body>
</html>
```